Tallgrove Vale Management

I need a professional website. My current website is tallgrovevalemanagement.com and I hate it. It was created with some AI tool very quickly because I needed a site up and running with no advanced notice. I’m open to all designs .. I trust you, the professionals will deliver the results I’m anxiously awaiting! :)

```html
<!DOCTYPE html>
<html lang="en">
<head>
<meta charset="utf-8">
<title>Tallgrove Vale Management</title>
<link href="https://fonts.googleapis.com/css2?family=Montserrat:wght@600;700;800&family=Fira+Sans:wght@400;500&display=swap" rel="stylesheet">
<style>
:root{
  --navy:#0e2748;
  --red:#c01d24;
  --red-deep:#b51a22;
  --white:#ffffff;
  --ink:#1f2a3a;
  --muted:#9fb0c8;
  --pale:#f3f5f8;
}
*{box-sizing:border-box;margin:0;padding:0}
html,body{width:1200px;height:2613px;overflow:hidden}
body{position:relative;background:var(--white);font-family:"Fira Sans",sans-serif;color:var(--ink)}
.abs{position:absolute}
.head{font-family:"Montserrat",sans-serif;font-weight:800;text-transform:uppercase;line-height:.95}
.brand{font-family:"Montserrat",sans-serif;font-weight:800;color:var(--navy);font-size:19px;line-height:1.15;letter-spacing:.5px}
.nav a{position:absolute;top:46px;font-family:"Montserrat",sans-serif;font-weight:600;font-size:13px;color:var(--navy);text-decoration:none}
.btn-red,.btn-white{position:absolute;display:flex;align-items:center;justify-content:center;font-family:"Montserrat",sans-serif;font-weight:600;font-size:13px;text-decoration:none}
.btn-red{background:var(--red);color:var(--white);clip-path:polygon(7% 0,100% 0,93% 100%,0 100%)}
.btn-white{background:var(--white);color:var(--navy);clip-path:polygon(7% 0,100% 0,93% 100%,0 100%)}
.photo{position:absolute}
.stat{position:absolute;top:855px;width:260px;text-align:center;color:var(--white)}
.stat .num{font-family:"Montserrat",sans-serif;font-weight:800;font-size:48px;margin-top:22px;letter-spacing:-1px}
.stat .lbl{font-family:"Montserrat",sans-serif;font-weight:600;font-size:18px;line-height:25px;margin-top:10px}
.divider{position:absolute;top:870px;width:1px;height:190px;background:#3a5478}
.eyebrow{font-family:"Montserrat",sans-serif;font-weight:800;font-size:12px;color:var(--red)}
.service{position:absolute;width:220px;text-align:center}
.service .lbl{font-family:"Montserrat",sans-serif;font-weight:700;font-size:15px;line-height:21px;color:var(--navy);margin-top:8px}
.step{position:absolute;top:1825px;width:220px;text-align:center;color:var(--white)}
.step .n{position:absolute;left:0;right:0;top:24px;font-family:"Montserrat",sans-serif;font-weight:800;font-size:26px;color:var(--red)}
.step .t{font-family:"Montserrat",sans-serif;font-weight:700;font-size:15px;margin-top:22px}
.step .d{font-size:17px;line-height:24px;margin-top:10px;color:#e4e9f1}
.fcol{position:absolute;top:2350px;color:var(--white)}
.fcol h4{font-family:"Montserrat",sans-serif;font-weight:600;font-size:20px;margin-bottom:20px}
.fcol a{display:block;color:var(--muted);font-size:15px;line-height:24px;text-decoration:none;margin-bottom:17px;letter-spacing:.4px}
.social{position:absolute;top:2497px;width:40px;height:40px;border-radius:50%;background:#2c4669}
</style>
</head>
<body>

<!-- header -->
<div class="abs brand" style="left:100px;top:52px;width:200px">TALLGROVE VALE<br>MANAGEMENT</div>
<div class="abs" style="left:100px;top:170px;width:100px;height:6px;background:var(--red)"></div>
<nav class="nav">
  <a style="left:356px">SERVICES</a>
  <a style="left:458px">OWNERS</a>
  <a style="left:555px">ABOUT</a>
  <a style="left:642px">RESOURCES</a>
  <a style="left:759px">CONTACT</a>
</nav>
<a class="btn-red" style="left:860px;top:27px;width:238px;height:52px">REQUEST A PROPOSAL</a>

<!-- hero -->
<svg class="abs" style="left:0;top:0" width="1200" height="800" aria-hidden="true">
  <path d="M0 160 L110 210 L40 420 L120 640 L0 700 Z" fill="var(--pale)"/>
</svg>
<div class="photo" role="img" aria-label="Modern white and navy apartment building at sunset"
  style="left:0;top:97px;width:1200px;height:688px;clip-path:polygon(785px 0,1200px 0,1200px 688px,445px 688px);background:linear-gradient(160deg,#7fa6cc 0%,#c9d6e2 35%,#e8e2d6 55%,#f2b560 80%,#3f4a2c 100%)"></div>
<svg class="abs" style="left:0;top:680px" width="1200" height="120" aria-hidden="true">
  <polygon points="680,5 1125,5 1080,105 0,105 0,105 620,105" fill="var(--navy)"/>
  <polygon points="1125,5 1200,5 1200,113 1080,113" fill="var(--red)"/>
</svg>
<div class="abs" style="left:655px;top:600px;width:392px;height:108px;background:var(--white);clip-path:polygon(12% 0,100% 0,90% 100%,0 100%)"></div>
<svg class="abs" style="left:738px;top:622px" width="58" height="66" viewBox="0 0 58 66" aria-hidden="true">
  <polygon points="29,2 55,17 55,49 29,64 3,49 3,17" fill="none" stroke="var(--navy)" stroke-width="2.5"/>
  <path d="M18 42 H40 M19 42 V34 M26 42 V30 M33 42 V36" stroke="var(--red)" stroke-width="2" fill="none"/>
  <path d="M18 32 L27 26 L33 30 L40 22" stroke="var(--red)" stroke-width="2" fill="none"/>
</svg>
<div class="abs head" style="left:809px;top:640px;font-size:15px;line-height:18px;color:var(--navy);font-weight:700">STRONGER ASSETS.<br>BETTER RETURNS.</div>

<h1 class="abs head" style="left:98px;top:222px;font-size:70px;color:var(--navy);line-height:64px">PROPERTY<br>MANAGEMENT</h1>
<div class="abs head" style="left:98px;top:358px;font-size:47px;color:var(--red);line-height:44px">BUILT AROUND<br>ASSET PROTECTION.</div>
<p class="abs" style="left:100px;top:478px;width:390px;font-size:17px;line-height:27.5px">Tallgrove Vale Management helps Ohio property owners and out-of-state investors protect rental assets, improve tenant experience, and manage operations with confidence.</p>
<a class="btn-red" style="left:100px;top:621px;width:240px;height:53px">REQUEST A PROPOSAL</a>
<a class="abs" style="left:354px;top:640px;font-family:Montserrat,sans-serif;font-weight:600;font-size:13px;color:var(--navy);text-decoration:none">FOR OWNERS <span style="color:var(--red);font-weight:800">&#8250;</span></a>

<!-- stats -->
<svg class="abs" style="left:0;top:785px" width="1200" height="360" aria-hidden="true">
  <polygon points="0,0 1200,0 1200,300 1140,358 60,358 0,300" fill="var(--navy)"/>
</svg>
<div class="divider" style="left:308px"></div>
<div class="divider" style="left:605px"></div>
<div class="divider" style="left:902px"></div>

<div class="stat" style="left:30px">
  <svg width="82" height="94" viewBox="0 0 82 94"><polygon points="41,2 80,24 80,70 41,92 2,70 2,24" fill="none" stroke="#fff" stroke-width="2.5"/><path d="M24 62 H58 M25 62 V52 M35 62 V46 M45 62 V52 M55 62 V40" stroke="var(--red)" stroke-width="2.5" fill="none"/><path d="M26 48 L38 42 L46 46 L56 36" stroke="var(--red)" stroke-width="2.5" fill="none"/></svg>
  <div class="num">98%</div><div class="lbl">OCCUPANCY<br>AVVERAGE</div>
</div>
<div class="stat" style="left:327px">
  <svg width="82" height="94" viewBox="0 0 82 94"><polygon points="41,2 80,24 80,70 41,92 2,70 2,24" fill="none" stroke="#fff" stroke-width="2.5"/><path d="M24 62 H58 M25 62 V52 M35 62 V46 M45 62 V52 M55 62 V40" stroke="var(--red)" stroke-width="2.5" fill="none"/><path d="M26 48 L38 42 L46 46 L56 36" stroke="var(--red)" stroke-width="2.5" fill="none"/></svg>
  <div class="num">$564M+</div><div class="lbl">ASSETS UNDER<br>MANAGEMENT</div>
</div>
<div class="stat" style="left:624px">
  <svg width="82" height="94" viewBox="0 0 82 94"><polygon points="41,2 80,24 80,70 41,92 2,70 2,24" fill="none" stroke="#fff" stroke-width="2.5"/><path d="M24 62 H58 M25 62 V52 M35 62 V46 M45 62 V52 M55 62 V40" stroke="var(--red)" stroke-width="2.5" fill="none"/><path d="M26 48 L38 42 L46 46 L56 36" stroke="var(--red)" stroke-width="2.5" fill="none"/></svg>
  <div class="num">$1.4M</div><div class="lbl">MAINTENANCE<br>COORDINATED</div>
</div>
<div class="stat" style="left:920px">
  <svg width="82" height="94" viewBox="0 0 82 94"><polygon points="41,2 80,24 80,70 41,92 2,70 2,24" fill="none" stroke="#fff" stroke-width="2.5"/><path d="M24 62 H58 M25 62 V52 M35 62 V46 M45 62 V52 M55 62 V40" stroke="var(--red)" stroke-width="2.5" fill="none"/><path d="M26 48 L38 42 L46 46 L56 36" stroke="var(--red)" stroke-width="2.5" fill="none"/></svg>
  <div class="num">12%+</div><div class="lbl">AVERAGE NOI<br>GROWTH</div>
</div>

<!-- services -->
<div class="photo" role="img" aria-label="Luxury lounge interior with city skyline view through tall windows"
  style="left:0;top:1280px;width:300px;height:323px;clip-path:polygon(0 0,300px 323px,0 323px);background:linear-gradient(160deg,#c8d6e4 0%,#8aa3bd 40%,#4a4f55 75%,#2c2a28 100%)"></div>
<div class="abs eyebrow" style="left:135px;top:1251px">OUR SERVICES</div>
<h2 class="abs head" style="left:135px;top:1282px;font-size:27px;color:var(--navy);line-height:27px">FULL-SERVICE.<br>OWNER FOCUSED.</h2>
<div class="abs" style="left:135px;top:1350px;width:100px;height:6px;background:var(--red)"></div>
<p class="abs" style="left:170px;top:1392px;width:320px;font-size:17px;line-height:27.5px;text-align:center">End-to end management solutions designed to protect your asset and elevate performance</p>

<div class="service" style="left:476px;top:1238px">
  <svg width="56" height="62" viewBox="0 0 56 62"><polygon points="28,2 53,16 53,46 28,60 3,46 3,16" fill="none" stroke="var(--red)" stroke-width="2"/><circle cx="28" cy="25" r="4" fill="none" stroke="var(--navy)" stroke-width="2"/><path d="M28 29 V34 M20 40 H36 V34 H20 Z" fill="none" stroke="var(--navy)" stroke-width="2"/></svg>
  <div class="lbl">PROPERTY<br>MANAGEMENT</div>
</div>
<div class="service" style="left:703px;top:1238px">
  <svg width="56" height="62" viewBox="0 0 56 62"><polygon points="28,2 53,16 53,46 28,60 3,46 3,16" fill="none" stroke="var(--red)" stroke-width="2"/><rect x="19" y="20" width="18" height="22" fill="none" stroke="var(--navy)" stroke-width="2"/><path d="M23 25 H26 M30 25 H33 M23 30 H26 M30 30 H33 M26 42 V36 H30 V42" stroke="var(--navy)" stroke-width="2" fill="none"/></svg>
  <div class="lbl">LEASE-UP &amp;<br>RENTAL MARKETING</div>
</div>
<div class="service" style="left:931px;top:1238px">
  <svg width="56" height="62" viewBox="0 0 56 62"><polygon points="28,2 53,16 53,46 28,60 3,46 3,16" fill="none" stroke="var(--red)" stroke-width="2"/><path d="M20 22 V40 H37 M25 36 V30 M30 36 V26 M35 36 V32" stroke="var(--navy)" stroke-width="2" fill="none"/></svg>
  <div class="lbl">FINANCIAL<br>MANAGEMENT</div>
</div>
<div class="service" style="left:486px;top:1395px">
  <svg width="56" height="62" viewBox="0 0 56 62"><polygon points="28,2 53,16 53,46 28,60 3,46 3,16" fill="none" stroke="var(--red)" stroke-width="2"/><path d="M20 22 L36 40 M36 22 L20 40 M18 24 L22 20 M34 38 L38 42" stroke="var(--navy)" stroke-width="2" fill="none"/></svg>
  <div class="lbl">MAINTENANCE<br>&amp; VENDOR MGMT</div>
</div>
<div class="service" style="left:707px;top:1395px">
  <svg width="56" height="62" viewBox="0 0 56 62"><polygon points="28,2 53,16 53,46 28,60 3,46 3,16" fill="none" stroke="var(--red)" stroke-width="2"/><circle cx="28" cy="25" r="5" fill="none" stroke="var(--navy)" stroke-width="2"/><path d="M18 41 Q28 28 38 41 Z" fill="none" stroke="var(--navy)" stroke-width="2"/></svg>
  <div class="lbl">TENANT RELIATONS<br>&amp; RETENTION</div>
</div>
<div class="service" style="left:925px;top:1395px">
  <svg width="56" height="62" viewBox="0 0 56 62"><polygon points="28,2 53,16 53,46 28,60 3,46 3,16" fill="none" stroke="var(--red)" stroke-width="2"/><path d="M21 20 H32 L37 25 V42 H21 Z M25 29 H33 M25 33 H33 M25 37 H33" stroke="var(--navy)" stroke-width="2" fill="none"/></svg>
  <div class="lbl">REPORTING &amp;<br>TRANSPARENCY</div>
</div>

<!-- lower background -->
<svg class="abs" style="left:0;top:1603px" width="1200" height="1010" aria-hidden="true">
  <rect x="0" y="139" width="1200" height="800" fill="var(--red-deep)"/>
  <rect x="0" y="200" width="20" height="230" fill="#c94048"/>
  <rect x="1176" y="200" width="24" height="230" fill="#c94048"/>
  <rect x="0" y="720" width="20" height="120" fill="#c94048"/>
  <rect x="1176" y="720" width="24" height="120" fill="#c94048"/>
  <polygon points="60,0 1140,0 1200,60 1200,139 1122,139 1122,427 1027,427 1027,455 165,455 165,427 72,427 72,139 0,139 0,60" fill="var(--navy)"/>
  <polygon points="165,692 1027,692 1027,717 1122,717 1122,857 1200,917 1200,1010 0,1010 0,917 72,857 72,717 165,717" fill="var(--navy)"/>
</svg>

<!-- process -->
<div class="abs eyebrow" style="left:142px;top:1674px">OUR PROCESS</div>
<h2 class="abs head" style="left:142px;top:1705px;font-size:27px;color:var(--white);line-height:27px">A BETTER WAY TO<br>MANAGE PROPERTY.</h2>
<div class="abs" style="left:142px;top:1775px;width:100px;height:6px;background:var(--red)"></div>
<svg class="abs" style="left:0;top:1855px" width="1200" height="20" aria-hidden="true">
  <g stroke="#b9c5d6" stroke-width="1.5" fill="#fff">
    <line x1="259" y1="10" x2="425" y2="10"/><circle cx="259" cy="10" r="3"/><circle cx="425" cy="10" r="3"/>
    <line x1="517" y1="10" x2="683" y2="10"/><circle cx="517" cy="10" r="3"/><circle cx="683" cy="10" r="3"/>
    <line x1="776" y1="10" x2="942" y2="10"/><circle cx="776" cy="10" r="3"/><circle cx="942" cy="10" r="3"/>
  </g>
</svg>
<div class="step" style="left:105px"><svg width="74" height="82" viewBox="0 0 74 82"><polygon points="37,2 72,21 72,61 37,80 2,61 2,21" fill="none" stroke="#fff" stroke-width="2"/></svg><div class="n">01</div><div class="t">ASSESS</div><div class="d">We evaluate your asset<br>and goals.</div></div>
<div class="step" style="left:361px"><svg width="74" height="82" viewBox="0 0 74 82"><polygon points="37,2 72,21 72,61 37,80 2,61 2,21" fill="none" stroke="#fff" stroke-width="2"/></svg><div class="n">02</div><div class="t">STRATEGIZE</div><div class="d">We build a custom plan<br>for performance</div></div>
<div class="step" style="left:620px"><svg width="74" height="82" viewBox="0 0 74 82"><polygon points="37,2 72,21 72,61 37,80 2,61 2,21" fill="none" stroke="#fff" stroke-width="2"/></svg><div class="n">03</div><div class="t">EXECUTE</div><div class="d">We handle the details<br>with precision.</div></div>
<div class="step" style="left:878px"><svg width="74" height="82" viewBox="0 0 74 82"><polygon points="37,2 72,21 72,61 37,80 2,61 2,21" fill="none" stroke="#fff" stroke-width="2"/></svg><div class="n">04</div><div class="t">OPTIMIZE</div><div class="d">We deliver results and<br>continuous improvement</div></div>

<!-- call to action -->
<h2 class="abs head" style="left:142px;top:2128px;font-size:27px;color:var(--white);line-height:27px">LET’S PROTECT YOUR<br>INVESTMENT TOGETHER.</h2>
<p class="abs" style="left:142px;top:2200px;font-size:17px;color:var(--white)">Get a custom management plan built around your goals.</p>
<a class="btn-white" style="left:725px;top:2151px;width:240px;height:52px">REQUEST A PROPOSAL</a>

<!-- footer -->
<div class="abs brand" style="left:120px;top:2385px;width:200px;color:var(--white)">TALLGROVE VALE<br>MANAGEMENT</div>
<div class="social" style="left:120px;background:var(--red)" role="img" aria-label="Social link"></div>
<div class="social" style="left:177px" role="img" aria-label="Social link"></div>
<div class="social" style="left:233px" role="img" aria-label="Social link"></div>
<div class="social" style="left:290px" role="img" aria-label="Social link"></div>

<div class="fcol" style="left:461px"><h4>About Us</h4><a>Our Story</a><a>Features</a><a>Our Team</a><a>Community</a></div>
<div class="fcol" style="left:643px"><h4>Support</h4><a>FAQ</a><a>Customer<br>Support</a><a>Contact Us</a></div>
<div class="fcol" style="left:825px"><h4>Company</h4><a>Why Us?</a><a>Our offers</a><a>Package</a><a>Management</a></div>
<div class="fcol" style="left:981px"><h4>Partners</h4><a>Our Partners</a><a>Become a<br>Partner</a></div>

</body>
</html>
```